Business Card Design Project

Business Card
We are rebranding with a new logo
Industry/Entity Type
Business
Contact Information for Business Card
Dennis Marlow +61 427581962 dennis@qovo.com.au P.O. Box 872 Kelvindale QLD 4309
Requirements
Must have
- Logo

```html
<!DOCTYPE html>
<html lang="en">
<head>
<meta charset="utf-8">
<title>Qovo International – Business Card</title>
<link href="https://fonts.googleapis.com/css2?family=Lexend:wght@400;500&display=swap" rel="stylesheet">
<style>
  :root {
    --backdrop: #e6e7e9;
    --card: #f7f7f6;
    --ink: #2b2b2d;
    --brand-blue: #2a8fcf;
    --accent-orange: #f07f1e;
    --card-shadow: rgba(0, 0, 0, 0.12);
  }
  * { margin: 0; padding: 0; box-sizing: border-box; }
  html, body {
    width: 1200px;
    height: 799px;
    overflow: hidden;
    background: var(--backdrop);
    font-family: "Lexend", "Helvetica Neue", Arial, sans-serif;
  }
  .business-card {
    position: absolute;
    left: 150px;
    top: 130px;
    width: 900px;
    height: 540px;
    background: var(--card);
    border-radius: 4px;
    box-shadow: 0 10px 30px var(--card-shadow);
  }
  .brand {
    position: absolute;
    left: 430px;
    top: 150px;
    display: flex;
    align-items: center;
    gap: 16px;
  }
  .brand-dot {
    width: 40px;
    height: 40px;
    border-radius: 50%;
    background: var(--brand-blue);
  }
  .brand-name {
    font-size: 34px;
    font-weight: 500;
    letter-spacing: 0.06em;
    text-transform: uppercase;
    color: var(--brand-blue);
  }
  .holder-name {
    position: absolute;
    left: 70px;
    top: 250px;
    font-size: 36px;
    font-weight: 400;
    color: var(--ink);
  }
  .contact-list {
    position: absolute;
    left: 430px;
    top: 290px;
    list-style: none;
  }
  .contact-item {
    display: flex;
    align-items: center;
    gap: 14px;
    height: 42px;
    font-size: 22px;
    color: var(--ink);
  }
  .contact-icon {
    width: 22px;
    height: 22px;
    fill: var(--accent-orange);
    flex: none;
  }
</style>
</head>
<body>
  <main class="business-card">
    <div class="brand">
      <span class="brand-dot"></span>
      <span class="brand-name">Qovo International</span>
    </div>

    <p class="holder-name">Dennis Marlow</p>

    <ul class="contact-list">
      <li class="contact-item">
        <svg class="contact-icon" viewBox="0 0 24 24" aria-hidden="true">
          <path d="M3 8c0-2 3-4 9-4s9 2 9 4v2h-5V8H8v2H3z"/>
          <rect x="5" y="11" width="14" height="9" rx="2"/>
        </svg>
        <span>+61 427581962</span>
      </li>
      <li class="contact-item">
        <svg class="contact-icon" viewBox="0 0 24 24" aria-hidden="true">
          <path d="M2 5h20v14H2z M3 6l9 7 9-7" stroke="#f7f7f6" stroke-width="1.5"/>
        </svg>
        <span>dennis@qovo.com.au</span>
      </li>
      <li class="contact-item">
        <svg class="contact-icon" viewBox="0 0 24 24" aria-hidden="true">
          <path d="M12 2a7 7 0 0 0-7 7c0 5 7 13 7 13s7-8 7-13a7 7 0 0 0-7-7zm0 10a3 3 0 1 1 0-6 3 3 0 0 1 0 6z"/>
        </svg>
        <span>P.O. Box 872 Kelvindale QLD 4309</span>
      </li>
    </ul>
  </main>
</body>
</html>
```